Cutting Board Oil and Finish

I designed these two labels and I am now wanting something a little more professional looking. The label should catch your eye, be unique but also professional. The design can also play off some of the ingredients too if you think that might look good ( beeswax, lemon oil, orange oil) I need two labels: One will be for the bottle of oil and the other will be for the bottle of finish. They are both the same brand so both labels should have the same theme and look related. The dimensions of the label for the bottle of oil will be 4 x 2.25 inches. The dimensions for the bottle of finish will be 3 x 2.125 inches
Anyone who uses cutting boards: moms, dads, chefs, woodworkers etc
It Professional

```html
<!DOCTYPE html>
<html lang="en">
<head>
<meta charset="utf-8">
<title>Holland's Cutting Board Finish Label</title>
<link rel="stylesheet" href="https://fonts.googleapis.com/css2?family=Space+Mono:ital,wght@1,700&family=Tenor+Sans&family=Arimo&display=swap">
<style>
  :root {
    --ink: #000000;
    --paper: #ffffff;
    --citrus: #f47b20;
  }
  html, body {
    margin: 0;
    padding: 0;
    width: 1200px;
    height: 1000px;
    overflow: hidden;
    background: var(--paper);
  }
  .canvas {
    position: relative;
    width: 1200px;
    height: 1000px;
    background: var(--paper);
    color: var(--ink);
  }
  .label-frame {
    position: absolute;
    left: 152px;
    top: 177px;
    width: 896px;
    height: 636px;
    box-sizing: border-box;
    border: 3px solid var(--ink);
    border-radius: 48px;
  }
  .brand-name {
    position: absolute;
    left: 0;
    width: 1200px;
    top: 232px;
    text-align: center;
    font-family: "Tenor Sans", sans-serif;
    font-size: 58px;
    line-height: 70px;
    letter-spacing: 2px;
    color: var(--ink);
  }
  .product-title {
    position: absolute;
    left: 0;
    width: 1200px;
    top: 342px;
    margin: 0;
    text-align: center;
    font-family: "Space Mono", monospace;
    font-style: italic;
    font-weight: 700;
    font-size: 84px;
    line-height: 104px;
    color: var(--ink);
  }
  .ingredient-pill {
    position: absolute;
    left: 301px;
    top: 587px;
    width: 600px;
    height: 92px;
    box-sizing: border-box;
    border: 3px solid var(--citrus);
    border-radius: 46px;
  }
  .ingredient-list {
    position: absolute;
    left: 0;
    width: 1200px;
    top: 596px;
    text-align: center;
    font-family: "Tenor Sans", sans-serif;
    font-size: 28px;
    line-height: 37px;
    color: var(--ink);
    word-spacing: 6px;
  }
  .ingredient-list .row-one { padding-left: 8px; }
  .ingredient-list .row-two { padding-right: 0; }
  .tagline {
    position: absolute;
    left: 0;
    width: 1200px;
    top: 706px;
    text-align: center;
    font-family: "Tenor Sans", sans-serif;
    font-size: 22px;
    line-height: 30px;
    color: var(--ink);
  }
  .volume {
    position: absolute;
    left: 0;
    width: 1200px;
    top: 762px;
    text-align: center;
    font-family: "Arimo", sans-serif;
    font-size: 24px;
    line-height: 30px;
    color: var(--ink);
  }
</style>
</head>
<body>
  <div class="canvas">
    <div class="label-frame"></div>
    <div class="brand-name">HOLLAND'S</div>
    <h1 class="product-title">CUTTING BOARD<br>FINISH</h1>
    <div class="ingredient-pill"></div>
    <div class="ingredient-list">
      <div class="row-one">Mineral oil&nbsp; Beeswax&nbsp; Carnauba wax</div>
      <div class="row-two">Orange oil&nbsp;&nbsp; Lemon oil</div>
    </div>
    <div class="tagline">all-natural and food-safe</div>
    <div class="volume">8FL OZ</div>
  </div>
</body>
</html>
```